Business Card Design Project for New Home Builder

Double sided card,
Larger logo on 1 side with small quote, Its not just a house, Its your Home, across the bottom. Matt Red base, White logo, black quote??

other side, ,
Its your Home LHS. Smaller logo RHS with.
Details below.

"neuropolitical Rg" Logo Font

Dennis Orford

PO Box 8437 Mildura VIC 3502
Mobile 0427 318865 / Phone 03 50718 962 / Fax 03 50718 415
email DennisO@tbvbuild.net.au
Vic Building Practitioner DB-U 8174 Vic Commercial Builder CB-U 5093
NSW Contractor Reg 37086C

Target Market(s)

New Home Buyers

Industry/Entity Type

Business

Requirements
Must have
• Sharp detail, Red Black & White colourings.
Should not have
• Any new colours

```html
<!DOCTYPE html>
<html lang="en">
<head>
<meta charset="utf-8">
<title>Dennis Orford Homes – Business Card</title>
<link rel="stylesheet" href="https://fonts.googleapis.com/css2?family=Montserrat:wght@400;500;600&family=Open+Sans:wght@400;600&display=swap">
<style>
  :root {
    --red: #ec1c24;
    --white: #ffffff;
    --ink: #222222;
    --grey: #6b6b6b;
    --stage: #ececec;
  }
  * { box-sizing: border-box; margin: 0; padding: 0; }
  html, body { width: 1200px; height: 1000px; overflow: hidden; }
  body {
    background: var(--stage);
    position: relative;
    font-family: "Open Sans", Arial, sans-serif;
  }
  .card {
    position: absolute;
    width: 640px;
    height: 366px;
    overflow: hidden;
    box-shadow: 0 6px 18px rgba(0,0,0,0.18);
  }
  .card--front { left: 110px; top: 100px; background: var(--red); }
  .card--back  { left: 450px; top: 530px; background: var(--white); }

  .brand { text-align: center; font-family: "Montserrat", Arial, sans-serif; font-weight: 600; }
  .brand__name { display: block; letter-spacing: 1px; line-height: 1; }
  .brand__sub  { display: block; letter-spacing: 6px; margin-top: 6px; }

  .card--front .brand { position: absolute; left: 0; right: 0; top: 118px; color: var(--white); }
  .card--front .brand__name { font-size: 44px; }
  .card--front .brand__sub  { font-size: 14px; }
  .tagline {
    position: absolute; left: 0; right: 0; top: 250px;
    text-align: center; color: var(--white);
    font-size: 17px; letter-spacing: 1.5px;
  }

  .card--back .brand { position: absolute; left: 250px; width: 330px; top: 78px; color: var(--ink); }
  .card--back .brand__name { font-size: 30px; }
  .card--back .brand__sub  { font-size: 10px; letter-spacing: 4px; }

  .person { position: absolute; left: 80px; top: 150px; }
  .person__name { color: var(--red); font-size: 20px; font-weight: 400; letter-spacing: 0.5px; }
  .person__role { color: var(--ink); font-size: 12px; margin-top: 2px; }

  .contact { position: absolute; left: 72px; top: 210px; list-style: none; }
  .contact__item { display: flex; align-items: flex-start; margin-bottom: 6px; }
  .contact__icon { width: 26px; flex: none; margin-right: 12px; display: flex; justify-content: center; }
  .contact__text { color: var(--ink); font-size: 13px; line-height: 18px; font-family: "Montserrat", Arial, sans-serif; }
  .contact__text--muted { color: var(--grey); }

  .accent { position: absolute; inset: 0; }
</style>
</head>
<body>

<section class="card card--front" aria-label="Card front">
  <div class="brand">
    <span class="brand__name">DENNIS ORFORD</span>
    <span class="brand__sub">HOMES</span>
  </div>
  <p class="tagline">Its not just a house, Its your Home</p>
</section>

<section class="card card--back" aria-label="Card back">
  <svg class="accent" viewBox="0 0 640 366" width="640" height="366" aria-hidden="true">
    <polygon points="330,366 640,150 640,200" fill="var(--red)"/>
    <polygon points="330,366 640,225 640,240" fill="var(--red)"/>
  </svg>

  <div class="brand">
    <span class="brand__name">DENNIS ORFORD</span>
    <span class="brand__sub">HOMES</span>
  </div>

  <div class="person">
    <p class="person__name">Alan Brooks</p>
    <p class="person__role">Director</p>
  </div>

  <ul class="contact">
    <li class="contact__item">
      <span class="contact__icon">
        <svg width="16" height="26" viewBox="0 0 16 26" aria-hidden="true"><rect x="1.5" y="1.5" width="13" height="23" rx="2.5" fill="none" stroke="var(--red)" stroke-width="2.4"/><circle cx="8" cy="20.5" r="1.4" fill="var(--red)"/></svg>
      </span>
      <span class="contact__text">0400 555 218<br>0355 501 732</span>
    </li>
    <li class="contact__item">
      <span class="contact__icon">
        <svg width="24" height="16" viewBox="0 0 24 16" aria-hidden="true"><rect width="24" height="16" rx="1.5" fill="var(--red)"/><polyline points="1,1.5 12,9 23,1.5" fill="none" stroke="var(--white)" stroke-width="1.6"/></svg>
      </span>
      <span class="contact__text contact__text--muted">alan.brooks@mailbox.net</span>
    </li>
    <li class="contact__item">
      <span class="contact__icon">
        <svg width="20" height="30" viewBox="0 0 20 30" aria-hidden="true"><path d="M10 1C5 1 1 5 1 10c0 7 9 19 9 19s9-12 9-19c0-5-4-9-9-9z" fill="var(--red)"/><circle cx="10" cy="10" r="3.6" fill="var(--white)"/></svg>
      </span>
      <span class="contact__text">27 Ridgeway Lane<br>Redcliff Vic 3496</span>
    </li>
  </ul>
</section>

</body>
</html>
```